Brindle Industries - Quality Campaign

Objective:

Create a visually engaging graphic design that promotes quality awareness and engagement within Brindle Industries. The design should convey the core values of quality at Brindle, emphasizing its four key elements:

Zero Defects, Zero Scrap
Customer Satisfaction
First Time Right
Product Performance
Target Audience:

Brindle Industries employees at all levels.

Usage:

The design will be used for various purposes, including:

Posters displayed in common areas and workstations
Presentation slides for internal meetings and training sessions
Design Requirements:

Visual Style: The design should be modern, professional, and visually appealing. It should evoke a sense of pride in quality and inspire team members to strive for excellence.
Color Palette: Consider using the Brindle Industries brand colors or a complementary palette that reflects quality and professionalism (see website: https://www.brindle-industries.example/).
Key Elements: The four key elements of quality should be clearly visible and integrated into the design. This could be achieved through text, icons, or a combination of both.
Brindle Industries Logo: A vector file of the Brindle Industries logo will be provided. Optional use of the logo is encouraged to maintain brand consistency.
Call to Action: The design should include a clear call to action, such as "Embrace Quality," "Strive for Excellence," or "Own Your Quality."
Additional Considerations:

Versatility: The design should be adaptable for different formats and sizes (e.g., posters, presentations, social media posts).
Memorability: The design should be memorable and easily recognizable as representing Brindle Industries' commitment to quality.
Deliverables:

High-resolution digital files in various formats suitable for printing and digital use.
By adhering to these guidelines, the winning design will effectively communicate the importance of quality at Brindle Industries and inspire employees to embrace these values in their daily work.

Industry/Entity Type

Engineering, manufacturing, semi-conductor, optics

Requirements
Must have
• Reference to Quality and 4 key elements

```html
<!DOCTYPE html>
<html lang="en">
<head>
<meta charset="utf-8">
<title>Brindle Industries – Embrace Quality</title>
<link rel="stylesheet" href="https://fonts.googleapis.com/css2?family=Montserrat:wght@700;800;900&display=swap">
<style>
  :root {
    --bg: #ffffff;
    --green: #95cc6a;
    --green-ink: #4f7f3a;
    --teal: #69c4c3;
    --teal-ink: #2a8d97;
    --red: #fe7676;
    --red-ink: #d12424;
    --gray: #bcbfbb;
    --gray-ink: #5f625f;
    --blue-light: #4fc3f7;
    --blue-dark: #1e6fd9;
    --white: #ffffff;
  }
  html, body {
    margin: 0;
    padding: 0;
    width: 749px;
    height: 1200px;
    overflow: hidden;
    background: var(--bg);
  }
  .canvas {
    position: relative;
    width: 749px;
    height: 1200px;
    display: flex;
    align-items: center;
    justify-content: center;
  }
  .quality-wheel { width: 560px; height: 560px; display: block; }
  .label {
    font-family: "Montserrat", sans-serif;
    font-weight: 800;
    font-size: 19px;
    text-anchor: middle;
  }
  .label--green { fill: var(--green-ink); }
  .label--teal { fill: var(--teal-ink); }
  .label--red { fill: var(--red-ink); }
  .label--gray { fill: var(--gray-ink); }
  .step-number {
    font-family: "Montserrat", sans-serif;
    font-weight: 800;
    font-size: 62px;
    fill: var(--white);
    text-anchor: middle;
    filter: drop-shadow(1px 2px 2px rgba(0,0,0,.3));
  }
  .badge-text {
    font-family: "Montserrat", sans-serif;
    font-weight: 800;
    font-size: 20px;
    letter-spacing: 3px;
    fill: var(--white);
    text-anchor: middle;
  }
  .icon { fill: none; stroke-width: 3.5; stroke-linecap: round; stroke-linejoin: round; }
  .icon--green { stroke: var(--green-ink); }
  .icon--teal { stroke: var(--teal-ink); }
  .icon--red { stroke: var(--red-ink); }
  .icon--gray { stroke: var(--gray-ink); }
</style>
</head>
<body>
<main class="canvas">
  <svg class="quality-wheel" viewBox="150 860 780 780" role="img" aria-label="Embrace Quality: four key elements of quality at Brindle Industries">
    <defs>
      <filter id="petal-shadow" x="-20%" y="-20%" width="140%" height="140%">
        <feDropShadow dx="0" dy="6" stdDeviation="9" flood-color="#000" flood-opacity=".28"/>
      </filter>
      <radialGradient id="badge-fill" cx="45%" cy="40%" r="65%">
        <stop offset="0" stop-color="var(--blue-light)"/>
        <stop offset=".6" stop-color="#38a8ee"/>
        <stop offset="1" stop-color="var(--blue-dark)"/>
      </radialGradient>
      <clipPath id="teal-area">
        <circle cx="645" cy="1145" r="270"/>
      </clipPath>
    </defs>

    <!-- Petals in swirl order: each overlaps the next -->
    <circle class="petal petal--green" cx="435" cy="1150" r="270" fill="var(--green)" filter="url(#petal-shadow)"/>
    <circle class="petal petal--gray" cx="445" cy="1360" r="270" fill="var(--gray)" filter="url(#petal-shadow)"/>
    <circle class="petal petal--red" cx="650" cy="1355" r="270" fill="var(--red)" filter="url(#petal-shadow)"/>
    <circle class="petal petal--teal" cx="645" cy="1145" r="270" fill="var(--teal)" filter="url(#petal-shadow)"/>
    <g clip-path="url(#teal-area)">
      <circle class="petal petal--green" cx="435" cy="1150" r="270" fill="var(--green)" filter="url(#petal-shadow)"/>
    </g>

    <!-- 01 Zero defects -->
    <g class="icon icon--green" transform="translate(313 1003)">
      <circle r="38" stroke-width="10" stroke-dasharray="10 9.9" fill="none"/>
      <circle r="38" fill="var(--green)"/>
      <circle r="38"/>
      <circle r="24"/>
      <path d="M-9 -9 L9 9 M9 -9 L-9 9"/>
    </g>
    <text class="label label--green" x="488" y="980">ZERO DEFECTS,</text>
    <text class="label label--green" x="488" y="1005">ZERO SCRAP</text>
    <text class="step-number" x="598" y="1082">01</text>

    <!-- 02 Customer satisfaction -->
    <g class="icon icon--teal" transform="translate(810 1105)">
      <path d="M-38 -36 l4 9 10 1 -7 7 2 10 -9 -5 -9 5 2 -10 -7 -7 10 -1z"/>
      <path d="M0 -56 l4 9 10 1 -7 7 2 10 -9 -5 -9 5 2 -10 -7 -7 10 -1z"/>
      <path d="M38 -36 l4 9 10 1 -7 7 2 10 -9 -5 -9 5 2 -10 -7 -7 10 -1z"/>
      <rect x="-42" y="20" width="16" height="34"/>
      <path d="M-26 24 h10 l10 -18 v-14 a6 6 0 0 1 12 2 v18 h20 a6 6 0 0 1 0 12 a6 6 0 0 1 0 12 a6 6 0 0 1 -2 12 h-40 z"/>
    </g>
    <text class="label label--teal" x="807" y="1218">CUSTOMER</text>
    <text class="label label--teal" x="807" y="1242">SATISFACTION</text>
    <text class="step-number" x="752" y="1332">02</text>

    <!-- 03 First time right -->
    <g class="icon icon--red" transform="translate(618 1520)">
      <circle r="44"/>
      <circle r="28"/>
      <circle r="11"/>
      <path d="M0 0 L34 -34"/>
      <path d="M28 -40 l6 -8 l6 8 l8 6 l-8 6 z" fill="var(--red-ink)"/>
    </g>
    <text class="label label--red" x="782" y="1484">FIRST TIME</text>
    <text class="label label--red" x="782" y="1507">RIGHT</text>
    <text class="step-number" x="467" y="1462">03</text>

    <!-- 04 Product performance -->
    <g class="icon icon--gray" transform="translate(275 1320)">
      <path d="M-38 10 V-20 M-46 -12 L-38 -22 L-30 -12"/>
      <path d="M-10 0 V-40 M-18 -32 L-10 -42 L-2 -32"/>
      <path d="M38 -10 V-52 M30 -44 L38 -54 L46 -44"/>
      <g transform="translate(-24 32)">
        <circle r="15" stroke-width="6" stroke-dasharray="5 4.4"/>
        <circle r="15" fill="var(--gray)"/>
        <circle r="15"/><circle r="6"/>
      </g>
      <g transform="translate(28 30)">
        <circle r="21" stroke-width="7" stroke-dasharray="6 5.5"/>
        <circle r="21" fill="var(--gray)"/>
        <circle r="21"/><circle r="10"/>
      </g>
    </g>
    <text class="label label--gray" x="276" y="1427">PRODUCT</text>
    <text class="label label--gray" x="276" y="1451">PERFORMANCE</text>
    <text class="step-number" x="334" y="1225">04</text>

    <!-- Call to action badge -->
    <g class="badge" transform="translate(543 1253)">
      <circle r="125" fill="url(#badge-fill)" filter="url(#petal-shadow)"/>
      <path d="M 25 -97 A 100 100 0 0 1 25 97" fill="none" stroke="var(--white)" stroke-width="20" stroke-dasharray="3.5 9.5"/>
      <path d="M -25 97 A 100 100 0 0 1 -25 -97" fill="none" stroke="var(--white)" stroke-width="20" stroke-dasharray="3.5 9.5"/>
      <text class="badge-text" x="0" y="-4">EMBRACE</text>
      <text class="badge-text" x="0" y="19">QUALITY</text>
    </g>
  </svg>
</main>
</body>
</html>
```